Brume d'Orvelle Hand Crafted Candles promotional flyer

Hand Crafted Soy Candles - I need a flyer to promote my candles and to give information on care of candles.I want this to use the design and colours I already have for my labels and the photo I have attached.I am aiming at a sophisticated market so would like to reflect this in the design.
Should appeal to sophisticated women who enjoy the pleasure of candles - to enhance their enjoyment of life - gives them the 'brume d'orvelle'.
the candles are hand crafted from all natural ingredients, environmentally friendly and with exquisite fragrances

Target Market(s)

sophisticated females

Industry/Entity Type

Promotional

Font styles to use
Script

Colors
cfeae6
ecdaeb

Requirements
Must have
• something expressing 'brume d'orvelle' - the enjoyment of candles
Should not have
• bright colours

```html
<!DOCTYPE html>
<html lang="en">
<head>
<meta charset="utf-8">
<title>Brume d'Orvelle Hand Crafted Candles – Flyer</title>
<link href="https://fonts.googleapis.com/css2?family=Mulish:wght@400;600;700;800&display=swap" rel="stylesheet">
<style>
  :root{
    --page:#ececec;
    --paper:#ffffff;
    --teal:#5ccab6;
    --teal-soft:#cfeae6;
    --purple:#8b45c2;
    --purple-deep:#6f2fa6;
    --purple-light:#a566d6;
    --lilac:#ecdaeb;
    --ink:#3b2f45;
    --skin-1:#c99a7f;
    --skin-2:#e8c3a8;
  }
  *{box-sizing:border-box;margin:0;padding:0}
  html,body{width:1200px;height:900px;overflow:hidden;background:var(--page);font-family:"Mulish",sans-serif;color:var(--ink)}
  .flyer{position:absolute;left:300px;top:26px;width:600px;height:848px;background:var(--paper);overflow:hidden;box-shadow:0 6px 18px rgba(0,0,0,.18)}
  .flyer-shapes{position:absolute;inset:0}
  .title{position:absolute;left:250px;top:34px;line-height:1}
  .title-main{font-size:31px;font-weight:800;color:var(--teal);letter-spacing:1px}
  .title-sub{font-size:17px;font-weight:700;color:#fff;margin-top:6px;padding-left:22px}
  .logo-badge{position:absolute;left:82px;top:326px;width:124px;height:124px;border-radius:50%;background:var(--lilac);border:4px solid var(--purple);display:flex;flex-direction:column;align-items:center;justify-content:center;text-align:center;color:var(--ink);font-size:14px;font-weight:700;line-height:1.2}
  .logo-badge small{font-size:8px;font-weight:700;letter-spacing:.5px;margin-top:4px;text-transform:uppercase}
  .product-shot{position:absolute;border-radius:50%}
  .product-shot--jar{left:202px;top:257px;width:96px;height:96px;border:6px solid var(--teal);background:radial-gradient(circle at 45% 45%,#2c2c34 0 32%,#7fbfb2 34% 100%)}
  .product-shot--pair{left:420px;top:155px;width:100px;height:100px;border:6px solid var(--lilac);background:radial-gradient(circle at 50% 55%,#3a3640 0 26%,#c9c4cc 28% 100%)}
  .col{position:absolute;font-size:7.9px;line-height:1.22}
  .col ul{list-style:none}
  .col li{position:relative;padding-left:12px;margin-bottom:1px}
  .col li::before{content:"";position:absolute;left:1px;top:2.5px;border-left:5px solid currentColor;border-top:3px solid transparent;border-bottom:3px solid transparent}
  .col--about{left:16px;top:458px;width:270px}
  .col--about li::before{color:var(--purple)}
  .brand-name{color:var(--purple);font-weight:800;font-size:9px}
  .tag-heading{display:inline-block;background:var(--teal);color:#fff;font-weight:800;font-size:11.5px;padding:1px 18px 1px 12px;margin:4px 0 3px;clip-path:polygon(0 0,100% 0,88% 100%,0 100%)}
  .section-heading{color:var(--purple);font-weight:800;font-size:11px;margin:4px 0 2px}
  .col--care{left:305px;top:355px;width:280px;color:#fff;font-size:8.5px;line-height:1.3}
  .care-heading{font-size:12.5px;font-weight:800;line-height:1.25;padding-bottom:6px;border-bottom:1px solid rgba(255,255,255,.7);margin-bottom:8px}
  .col--care li{margin-bottom:3px}
  .col--care li::before{color:#fff}
  .contact{position:absolute;left:18px;top:774px;width:270px;font-size:13.5px;font-weight:600;color:var(--ink);line-height:1.45;font-style:normal}
  .contact-row{display:flex;align-items:center;gap:8px}
  .contact-row svg{width:13px;height:13px;flex:none}
</style>
</head>
<body>
<main class="flyer">
  <svg class="flyer-shapes" viewBox="0 0 600 848" width="600" height="848">
    <defs>
      <linearGradient id="photoTone" x1="0" y1="0" x2="1" y2="1">
        <stop offset="0" stop-color="#e8c3a8"/>
        <stop offset="1" stop-color="#c99a7f"/>
      </linearGradient>
      <linearGradient id="purplePanel" x1="0" y1="0" x2="1" y2="1">
        <stop offset="0" stop-color="#a566d6"/>
        <stop offset="1" stop-color="#6f2fa6"/>
      </linearGradient>
    </defs>
    <rect class="hero-photo" x="0" y="0" width="600" height="390" fill="url(#photoTone)" role="img" aria-label="Photograph of a smiling woman relaxing beside a lit candle"/>
    <path class="panel-care" d="M600,120 C480,150 340,250 292,350 L292,848 L600,848 Z" fill="url(#purplePanel)"/>
    <path class="panel-about" d="M0,390 C90,345 210,330 292,352 L292,848 L0,848 Z" fill="#ffffff"/>
    <path class="panel-about-edge" d="M0,390 C90,345 210,330 292,352" fill="none" stroke="#8b45c2" stroke-width="5"/>
    <rect class="contact-band" x="0" y="766" width="292" height="82" fill="#5ccab6"/>
  </svg>

  <header class="title">
    <div class="title-main">BRUME D'ORVELLE -</div>
    <div class="title-sub">The enjoyment of candles</div>
  </header>

  <div class="product-shot product-shot--pair" role="img" aria-label="Photo of two candle jars on a shelf"></div>
  <div class="product-shot product-shot--jar" role="img" aria-label="Photo of a black candle jar with label"></div>

  <div class="logo-badge">Brume d'Orvelle<small>Hand Crafted Candles</small></div>

  <section class="col col--about">
    <ul>
      <li><span class="brand-name">Brume d'Orvelle</span> – an exuberant enjoyment of life – these candles will fill you with "Brume d'Orvelle".</li>
      <li>Candles are lovingly hand-poured and use only the finest of ingredients and fragrances</li>
      <li>Hand crafted soy candle creations</li>
      <li>Completely non-toxic</li>
      <li>Exquisite fragrances</li>
      <li>Clean burning</li>
      <li>Environmentally friendly.</li>
    </ul>
    <div class="tag-heading">Why soy wax?</div>
    <ul>
      <li>Soft smooth wax that burns clear – no soot or smoke</li>
      <li>Soy wax candles burn up to 50% longer than traditional paraffin candles</li>
      <li>Made from soya beans, a renewable natural resource that supports and sustains agriculture – it is biodegradable and environmentally friendly.</li>
      <li>Soy wax burns cooler than paraffin and disperse the fragrance more fully.</li>
    </ul>
    <h3 class="section-heading">Containers can be refilled</h3>
    <ul>
      <li>I offer a refill service: if you return your containers to me I can refill with the fragrance of your choice</li>
      <li>Or if you have a special container you would like to use for your candle just contact me for a quote.</li>
      <li>I have a wide range of fragrances - please contact me for details.</li>
    </ul>
  </section>

  <section class="col col--care">
    <h2 class="care-heading">How to care for your candle – the following tips will ensure you have a long lasting, fully fragranced candle</h2>
    <ul>
      <li>When lighting your candle for the first time, allow the wax to melt all the way to the sides of the container. This creates a 'memory' and avoids 'tunnelling' as the candle burns.</li>
      <li>Always trim the wick to about 6-8mm before relighting your candle. This will ensure a long lasting candle, minimise soot and remove any mushrooming of the wick from a previous burn.</li>
      <li>It is preferable to use a candle 'snuffer' to extinguish the flame or a lid if the candle has one. Alternatively you can dip the wick into the melted wax and then straighten. This will stop the wick from smoking and help with relighting.</li>
      <li>All Brume d'Orvelle candles are hand poured not mass produced – although every effort is made to ensure consistency every candle may be different.</li>
      <li>Sometimes you may notice darker patches or wet spots – this is not a fault it's just the natural way the wax has set – it does not affect the candle in any way.</li>
      <li>The top of the candle may also appear slightly uneven – this is just a sign of natural soy wax being hand poured.</li>
      <li>Do not leave your candle in the sunlight as it may turn a yellow colour – again this does not affect the candle in anyway – it just loses its creamy white colour.</li>
      <li>As these candles contain no preservatives or chemicals it is recommended that they should be used within 6 months.</li>
    </ul>
  </section>

  <address class="contact">
    <div class="contact-row">
      <svg viewBox="0 0 16 16"><path d="M3 1.5l3 .5 1 3.2-1.8 1.3a9 9 0 0 0 4.3 4.3L10.8 9l3.2 1 .5 3-2 2C6.5 15 1 9.5 1 3.5z" fill="#3b2f45"/></svg>
      <span>021 555 0148</span>
    </div>
    <div class="contact-row">
      <svg viewBox="0 0 16 16"><rect x="1" y="3" width="14" height="10" rx="1" fill="#3b2f45"/><path d="M1.5 3.8L8 9l6.5-5.2" fill="none" stroke="#5ccab6" stroke-width="1.3"/></svg>
      <span>clara.hewitt@brumemail.co.nz</span>
    </div>
    <div class="contact-row">
      <svg viewBox="0 0 16 16"><circle cx="8" cy="8" r="6.5" fill="none" stroke="#3b2f45" stroke-width="1.5"/><ellipse cx="8" cy="8" rx="2.8" ry="6.5" fill="none" stroke="#3b2f45" stroke-width="1.2"/><path d="M1.5 8h13" stroke="#3b2f45" stroke-width="1.2"/></svg>
      <span>www.mybrumedorvelle.co.nz</span>
    </div>
  </address>
</main>
</body>
</html>
```